WALKING FOOD TOURISM BUSINESS. REQUEST FOR DIGITAL BROCHURE

Our business is a walking food tourism business in and around Melbourne's central city. We are needing a e-digital brochure - to be solely used as email' marketing content, not print. Therefore PDF size needs to be appropriate/suitable. Please see attached written content required for the brochure - together with our logo. For images, I am happy for designer to use our website content (www.wanderplatekitchen.com). OR any other appropriate and creative 'foodie' or Melbourne image suitable. Many thanks:)

Target Market(s)

Premium brand travellers or local adventurous Australians.

Requirements
Must have
• Quality font and images
Nice to have
• Quality Melbourne and food images. See website - wanderplatekitchen.com
Should not have
• Too much colour. Brand is black and white, sophisticated, premium product.

```html
<!DOCTYPE html>
<html lang="en">
<head>
<meta charset="utf-8">
<title>Wanderplate Kitchen – Gourmet Walking Food Tours Brochure</title>
<link href="https://fonts.googleapis.com/css2?family=Kaushan+Script&family=Open+Sans:wght@400;600;700&display=swap" rel="stylesheet">
<style>
  :root {
    --canvas: #e8e8e8;
    --paper: #ffffff;
    --ink: #1c1c1c;
    --muted: #555555;
    --navy: #1f3546;
    --rule: #cfcfcf;
    --blush-a: #e9d6da;
    --blush-b: #f6eef0;
  }
  * { box-sizing: border-box; margin: 0; padding: 0; }
  html, body { width: 1200px; height: 900px; overflow: hidden; }
  body {
    background: var(--canvas);
    font-family: "Open Sans", Arial, sans-serif;
    color: var(--ink);
    position: relative;
  }
  .page {
    position: absolute;
    top: 202px;
    width: 350px;
    height: 495px;
    background: var(--paper);
    overflow: hidden;
  }
  .page--about { left: 50px; border-right: 1px solid var(--rule); }
  .page--experiences { left: 400px; }
  .page--cover { left: 810px; }

  .script { font-family: "Kaushan Script", cursive; font-weight: 400; }
  .brand-name {
    font-size: 11px; font-weight: 600; letter-spacing: 0.5px;
    color: var(--ink); display: flex; align-items: center; gap: 5px;
  }
  .brand-name::before {
    content: ""; width: 7px; height: 7px; background: var(--ink); display: block;
  }
  .photo { display: block; }
  .site-url {
    position: absolute; bottom: 14px; left: 0; right: 0;
    text-align: center; font-size: 7px; letter-spacing: 2px; color: var(--muted);
  }

  /* About page */
  .about__header { height: 62px; background: linear-gradient(100deg, var(--blush-a), var(--blush-b) 60%, #ffffff); }
  .about__brand { position: absolute; top: 70px; right: 22px; }
  .about__bar { position: absolute; top: 95px; left: 22px; width: 150px; height: 6px; background: var(--ink); }
  .about__title { position: absolute; top: 104px; right: 24px; font-size: 30px; }
  .about__text { position: absolute; top: 150px; left: 24px; right: 24px; font-size: 7px; line-height: 1.55; text-align: justify; }
  .about__text p + p { margin-top: 6px; }
  .about__divider { position: absolute; top: 240px; left: 24px; right: 24px; height: 2px; background: var(--ink); }
  .about__gallery {
    position: absolute; top: 254px; left: 24px; right: 24px; height: 200px;
    display: grid; grid-template-columns: 1.1fr 1fr; grid-template-rows: 1fr 1fr; gap: 6px;
  }
  .about__gallery .photo--night { grid-row: 1 / span 2; background: linear-gradient(160deg, #2b2a38, #5b4a3e 55%, #a7763e); }
  .about__gallery .photo--city { background: linear-gradient(180deg, #6f9ed4, #b9cfe6 55%, #6e7f74); }
  .about__gallery .photo--team { background: linear-gradient(180deg, #9aa4ae, #3d3f43); }

  /* Experiences page */
  .exp__header {
    height: 82px; position: relative;
    background: linear-gradient(100deg, #ead9dd, #f3ebe6 45%, #dbe6de 80%, #c9d9e1);
  }
  .exp__title { position: absolute; bottom: 4px; left: 0; right: 0; text-align: center; font-size: 30px; color: var(--ink); }
  .exp__intro { margin: 10px 26px 6px; font-size: 6.8px; line-height: 1.5; text-align: center; color: var(--muted); }
  .tour { margin: 0 26px 7px; text-align: center; }
  .tour__name {
    display: inline-block; background: var(--navy); color: #fff;
    font-size: 7px; font-weight: 700; letter-spacing: 1px; padding: 2px 14px; text-transform: uppercase;
  }
  .tour__details { font-size: 8px; font-weight: 700; margin: 3px 0 2px; }
  .tour__desc { font-size: 6.6px; line-height: 1.5; color: var(--muted); }

  /* Cover */
  .cover__brand { position: absolute; top: 36px; right: 28px; font-size: 12px; }
  .cover__photo {
    position: absolute; top: 76px; left: 0; right: 0; height: 200px;
    background: linear-gradient(180deg, #4d8fd6 0%, #a9c9ea 38%, #6b7f6a 62%, #3f5a63 100%);
  }
  .cover__band {
    position: absolute; top: 276px; left: 0; right: 0; height: 26px; background: var(--navy);
    display: flex; justify-content: space-around; align-items: center;
    color: #fff; font-size: 6.5px; letter-spacing: 0.3px;
  }
  .cover__title { position: absolute; top: 322px; left: 0; right: 0; text-align: center; font-size: 46px; line-height: 1; }
  .cover__url { position: absolute; top: 376px; left: 0; right: 0; text-align: center; font-size: 6.5px; letter-spacing: 2px; color: var(--muted); }
  .cover__subtitle { position: absolute; top: 388px; left: 0; right: 0; text-align: center; font-size: 15px; font-weight: 600; letter-spacing: 0.5px; }
  .cover__rule { position: absolute; top: 418px; left: 110px; right: 110px; height: 1px; background: var(--ink); }
</style>
</head>
<body>

  <section class="page page--about">
    <div class="about__header photo" role="img" aria-label="Soft blush photo of a dining table"></div>
    <div class="about__brand brand-name">Wanderplate Kitchen</div>
    <div class="about__bar"></div>
    <h2 class="about__title script">about us</h2>
    <div class="about__text">
      <p>We provide experiential adventures for visitors and locals alike, all through the lens of exceptional food, coffee and wine found in the heart of the city.</p>
      <p>Born and raised here, our guides share the people, places and flavours that make these streets special, one small plate at a time.</p>
    </div>
    <div class="about__divider"></div>
    <div class="about__gallery">
      <div class="photo photo--night" role="img" aria-label="Guests at a busy laneway bar at night"></div>
      <div class="photo photo--city" role="img" aria-label="City skyline above the river"></div>
      <div class="photo photo--team" role="img" aria-label="Tour guides standing together in a restaurant"></div>
    </div>
    <p class="site-url">www.wanderplatekitchen.com</p>
  </section>

  <section class="page page--experiences">
    <div class="exp__header photo" role="img" aria-label="Wine glasses on a sunlit table">
      <h2 class="exp__title script">Our Experiences</h2>
    </div>
    <p class="exp__intro">Take a stroll through Melbourne's laneways and taste the stories behind its kitchens, cafés and markets with a local guide who knows every corner.</p>

    <article class="tour">
      <h3 class="tour__name">Grand Tasting Trail</h3>
      <p class="tour__details">3.5 hours / A$145 Adult / A$105 Child / Up to 8 guests</p>
      <p class="tour__desc">Our signature walk visits the city's most loved kitchens, from hidden laneway bars to market stalls, with tastings at every stop along the way.</p>
    </article>
    <article class="tour">
      <h3 class="tour__name">Laneway Bites Walk</h3>
      <p class="tour__details">3 hours / A$98 Adult / A$62 Child / Up to 10 guests</p>
      <p class="tour__desc">Follow the smell of fresh bread and grilled skewers through busy arcades, sampling the casual bites that locals queue for every single day.</p>
    </article>
    <article class="tour">
      <h3 class="tour__name">Old Town Flavours</h3>
      <p class="tour__details">2.5 hours / A$79 Adult / A$45 Child / Up to 12 guests</p>
      <p class="tour__desc">Walk the old streets where the city began and hear how gold, migration and markets shaped the food we share on our tables today.</p>
    </article>
    <article class="tour">
      <h3 class="tour__name">Twilight Wine &amp; Plates</h3>
      <p class="tour__details">3 hours / A$185 Adult / A$140 Child / Up to 8 guests</p>
      <p class="tour__desc">As the lights come on, settle into intimate venues for matched plates and local wines, finishing with a sweet treat by the river.</p>
    </article>
    <article class="tour">
      <h3 class="tour__name">Bespoke Group Walks</h3>
      <p class="tour__details">Up to 6 hours / Custom routes</p>
      <p class="tour__desc">Planning a celebration or team outing? We build a route around your group, your tastes and your timing, from a short stroll to a full day.</p>
    </article>
    <p class="site-url">www.wanderplatekitchen.com</p>
  </section>

  <section class="page page--cover">
    <div class="cover__brand brand-name">Wanderplate Kitchen</div>
    <div class="cover__photo photo" role="img" aria-label="Riverside view of the city with a footbridge and blossom tree"></div>
    <div class="cover__band">
      <span>IG - wanderplatekitchen</span>
      <span>FB - WanderplateKitchen</span>
      <span>+61 400 000 123</span>
      <span>info@wanderplatekitchen.com</span>
    </div>
    <h1 class="cover__title script">Melbourne</h1>
    <p class="cover__url">www.wanderplatekitchen.com</p>
    <p class="cover__subtitle">Gourmet Walking Food Tours</p>
    <div class="cover__rule"></div>
  </section>

</body>
</html>
```